Corporate Financial Services

This is a new Company. The ROW represents my son's and my own Christian name initials (ROW) (Colin and Brent) but no real significance.
This is a boutique financial services company active in the full parameter of corporate and business transactions. From standard financial and tax services to specialised Research & Development, mergers and acquisitions, business valuations, and capital raising.
Over 30 years of experience with listed and private entities.
I am after something exciting, given the nature of the business, bright, clean and colourful, but not in comic form.
Hi there,
Firstly thankyou for accepting the challenge. I have no ideas and nothing to compare your submissions with other than other peoples cards.
A few points
I omitted the ABN number from the card description. This is an important reference for all businesses operating in Australia. Therefore the following should be shown in association with the company name ROW Corporate & Financial Services Pty Ltd It can either be within brackets or without but always shown underneath the company name in smaller font.
The eight core business services need to be shown on the reverse
My contact number should also be shown along side the address
My business title is Chartered Accountant in full. I am also not fussed as to whether my name appears in caps or Caps and lowercase ie Brent Ashdown or BRENT ASHDOWN but this will depend upon the design of the rest of the card.
Maybe a small logo for the company needs to be attached but not sure.
Kind regards
Brent Ashdown
Financial
ROW Corporate & Financial Services Pty Ltd
(ABN 71 309 482 157)
(Note ABN could be shown on the reverse side with just ROW Corporate & Financial Services Pty Ltd on the front....no ABN
17 Wattlebank Street Norvale SA 5174
Brent Ashdown
Chartered Accountant
Phone (symbol preferred) +61 (0) 437 215604
Email (symbol) to be provided
www.rowfinsvc-example.com.au
Skype brent7312
- On the reverse:
Corporate Finance
Taxation
Research & Development Specialisation
Financial Accounting
Mergers & Acquisitions
Company Listings (IPO's)
Business Valuations
Capital Raising
- Interested in a strong black card (or grey white platinum and black colours) with either platinum or gold highlight modern name style no italics. I would also like at a later stage with the winner to use this same design for card for Asia with a red and or gold and platinum colour. But I want this batch first.
The smart block (square) for digital image transfer to mobile phones contained within a gold or platinum square border on reverse of the card
Anything old or staid looking. No italics sans serif

```html
<!DOCTYPE html>
<html lang="en">
<head>
<meta charset="utf-8">
<title>ROW Corporate &amp; Financial Services – Business Card</title>
<link rel="stylesheet" href="https://fonts.googleapis.com/css2?family=Noto+Serif:wght@400&family=Open+Sans:wght@400;600;700&display=swap">
<style>
  :root {
    --page-bg: #dcd9d3;
    --band-white: #f7f7f7;
    --band-text: #3a3a3a;
    --mark-dark: #2e2e2e;
    --contact-text: #f2f2f2;
    --contact-muted: #cfcfcf;
  }
  * { box-sizing: border-box; margin: 0; padding: 0; }
  html, body {
    width: 1200px;
    height: 1024px;
    overflow: hidden;
    background: var(--page-bg);
  }
  .business-card {
    position: absolute;
    left: 100px;
    top: 226px;
    width: 1000px;
    height: 572px;
    border-radius: 6px;
    overflow: hidden;
    box-shadow: 0 12px 30px rgba(0,0,0,0.25);
  }
  .card-surface {
    position: absolute;
    inset: 0;
    width: 100%;
    height: 100%;
  }
  .company-band {
    position: absolute;
    left: 0;
    top: 362px;
    width: 520px;
    height: 112px;
    background: var(--band-white);
    display: flex;
    align-items: center;
    gap: 24px;
    padding-left: 44px;
  }
  .company-square {
    width: 52px;
    height: 52px;
    background: var(--mark-dark);
    flex: none;
  }
  .company-name {
    font-family: "Noto Serif", serif;
    font-weight: 400;
    font-size: 34px;
    line-height: 1.12;
    color: var(--band-text);
  }
  .company-name .suffix {
    font-size: 13px;
    vertical-align: super;
    margin-left: 4px;
  }
  .contact-block {
    position: absolute;
    right: 44px;
    top: 44px;
    text-align: right;
    font-family: "Open Sans", sans-serif;
    color: var(--contact-text);
  }
  .person-name {
    font-size: 34px;
    font-weight: 700;
    line-height: 1.2;
  }
  .person-title {
    font-size: 21px;
    font-weight: 400;
    color: var(--contact-muted);
    margin-bottom: 20px;
  }
  .contact-line, .address-line {
    display: flex;
    justify-content: flex-end;
    align-items: center;
    gap: 10px;
    font-size: 16px;
    font-weight: 600;
    line-height: 1.7;
    white-space: nowrap;
  }
  .contact-line svg, .address-line svg { flex: none; }
  .address-block {
    position: absolute;
    right: 44px;
    bottom: 40px;
    text-align: right;
    font-family: "Open Sans", sans-serif;
    color: var(--contact-text);
  }
</style>
</head>
<body>
  <article class="business-card">
    <svg class="card-surface" viewBox="0 0 1000 572" preserveAspectRatio="none" aria-hidden="true">
      <defs>
        <linearGradient id="greyBase" x1="0" y1="0" x2="1" y2="1">
          <stop offset="0" stop-color="#c9c9c9"/>
          <stop offset="1" stop-color="#a7a7a7"/>
        </linearGradient>
        <pattern id="diagonalStripes" width="64" height="64" patternUnits="userSpaceOnUse" patternTransform="rotate(-21)">
          <rect width="32" height="64" fill="#ffffff" fill-opacity="0.18"/>
        </pattern>
        <linearGradient id="blackPanel" x1="0" y1="0" x2="0.3" y2="1">
          <stop offset="0" stop-color="#2f2f30"/>
          <stop offset="0.55" stop-color="#1b1b1c"/>
          <stop offset="1" stop-color="#111112"/>
        </linearGradient>
      </defs>
      <rect class="stripe-field" width="1000" height="572" fill="url(#greyBase)"/>
      <rect width="1000" height="572" fill="url(#diagonalStripes)"/>
      <polygon class="black-panel" points="330,0 1000,0 1000,572 470,572" fill="url(#blackPanel)"/>
    </svg>

    <div class="company-band">
      <span class="company-square"></span>
      <p class="company-name">ROW Corporate &amp;<br>Financial Services<span class="suffix">Pty Ltd</span></p>
    </div>

    <div class="contact-block">
      <p class="person-name">Brent Ashdown</p>
      <p class="person-title">Chartered Accountant</p>
      <p class="contact-line">
        <svg width="13" height="19" viewBox="0 0 14 20"><rect x="1" y="1" width="12" height="18" rx="2" fill="none" stroke="#f2f2f2" stroke-width="2"/><circle cx="7" cy="15.5" r="1.3" fill="#f2f2f2"/></svg>
        +61 (0) 437 215604
      </p>
      <p class="contact-line">
        <svg width="18" height="13" viewBox="0 0 20 14"><rect x="1" y="1" width="18" height="12" fill="none" stroke="#f2f2f2" stroke-width="2"/><path d="M1 1 L10 8 L19 1" fill="none" stroke="#f2f2f2" stroke-width="2"/></svg>
        brent@rowfinsvc-example.com.au
      </p>
      <p class="contact-line">
        <svg width="16" height="16" viewBox="0 0 18 18"><circle cx="9" cy="9" r="8" fill="#f2f2f2"/></svg>
        brent7312
      </p>
    </div>

    <div class="address-block">
      <p class="address-line">
        <svg width="16" height="16" viewBox="0 0 18 18"><circle cx="9" cy="9" r="7.5" fill="none" stroke="#f2f2f2" stroke-width="2"/><ellipse cx="9" cy="9" rx="3.2" ry="7.5" fill="none" stroke="#f2f2f2" stroke-width="1.5"/><line x1="1.5" y1="9" x2="16.5" y2="9" stroke="#f2f2f2" stroke-width="1.5"/></svg>
        www.rowfinsvc-example.com.au | ABN 71 309 482 157
      </p>
      <p class="address-line">
        <svg width="13" height="19" viewBox="0 0 14 20"><path d="M7 19 C3 13 1 10 1 7 A6 6 0 0 1 13 7 C13 10 11 13 7 19 Z" fill="#f2f2f2"/><circle cx="7" cy="7" r="2.2" fill="#1b1b1c"/></svg>
        17 Wattlebank Street Norvale SA 5174
      </p>
    </div>
  </article>
</body>
</html>
```